Can you make our site AWESOME?

Hi Guys,

I am a co-founder of Tumble Crate Rentals Oz, the world's first e-commerce skip bin business.

We are looking to update our site before a launch into the UK in March.

Please help us by submitting your designs for the following pages:

- Home page (www.tumblecraterentalsoz.example.au)
- About us (https://www.tumblecraterentalsoz.example.au/pages/about-us
- Contact us (https://www.tumblecraterentalsoz.example.au/pages/contact-us)
- Quick Quote / Pricing (https://www.tumblecraterentalsoz.example.au/pages/free-instant-quote-skip-bin-hire)

NOTES:
- Design should be high-converting
- best designs will be fresh, modern, easy to read, distinctive and memorable
- please use our logo and video colours
- feel free to change logos, layout, images and anything else you feel can be improved
- the winning designer will potentially have the opportunity to re-design the other pages on our site
- brief is for design only

Any questions just ask.

Thanks,
Morton

```html
<!DOCTYPE html>
<html lang="en">
<head>
<meta charset="utf-8">
<title>Tumble Crate Rentals Oz</title>
<link rel="stylesheet" href="https://fonts.googleapis.com/css2?family=Oswald:wght@500;600&family=Open+Sans:wght@400;600;700&display=swap">
<style>
:root{
  --indigo:#2b0fa0;
  --indigo-deep:#22098a;
  --indigo-mid:#3018a6;
  --green:#0c8a3e;
  --green-light:#2fc46a;
  --navy:#150650;
  --grey:#ececef;
  --grey-line:#dcdce2;
  --ink:#141414;
  --body:#444;
  --white:#fff;
  --faint-num:#b9e6c8;
}
*{box-sizing:border-box;margin:0;padding:0}
html,body{width:1200px;height:4235px;overflow:hidden}
body{position:relative;background:var(--grey);font-family:"Open Sans",Arial,sans-serif;color:var(--ink)}
.abs{position:absolute}
.hero{left:0;top:0;width:1200px;height:678px;background:linear-gradient(120deg,#2a0c9c 0%,#3316b0 55%,#2a0c9c 100%)}
.nav{left:124px;top:28px;width:952px;height:40px;display:flex;align-items:center;color:var(--white)}
.brand{font-family:"Oswald",sans-serif;font-weight:600;font-size:17px;letter-spacing:.5px;text-transform:uppercase;line-height:1}
.nav-links{position:absolute;left:186px;top:12px;display:flex;gap:0;font-size:12px;font-weight:600;letter-spacing:1px}
.nav-links span{position:absolute;white-space:nowrap}
.nav-links .active{color:var(--green-light)}
.sec-num{font-family:"Oswald",sans-serif;font-weight:500;font-size:64px;line-height:1;color:var(--faint-num);opacity:.55}
.sec-title{font-family:"Oswald",sans-serif;font-weight:600;line-height:1.1}
.kicker{font-size:11px;font-weight:700;letter-spacing:1.5px;color:var(--green);text-transform:uppercase}
.rule{width:3px;background:var(--green-light)}
.search{display:flex;height:42px;border-radius:21px;background:var(--white);overflow:hidden;align-items:center}
.search .field{flex:1;padding-left:30px;font-size:16px;font-style:italic;color:#aaa}
.search .btn{height:42px;width:120px;background:var(--green);color:var(--white);font-weight:700;font-size:14px;letter-spacing:1px;display:flex;align-items:center;justify-content:center;gap:10px;border-radius:21px}
.photo{background:linear-gradient(160deg,#6b5a4f,#8e6f5a 45%,#c9c6c2);}
.step{top:790px;height:212px;padding:40px 40px 0 40px}
.step .n{font-family:"Oswald",sans-serif;font-size:22px;line-height:1}
.step .lbl{font-size:10px;font-weight:700;letter-spacing:1.3px;text-transform:uppercase;margin:6px 0 8px}
.step p{font-size:17px;font-weight:700;line-height:1.35}
p.copy{font-size:13px;line-height:1.6;color:var(--body)}
.cell{height:0;padding:28px 30px 0 92px;color:var(--white)}
.cell .tag{font-size:10px;font-weight:700;letter-spacing:1.2px;text-transform:uppercase}
.cell .txt{font-size:17px;font-weight:700;line-height:1.3;margin-top:6px}
.cell .more{position:absolute;right:30px;bottom:20px;font-size:11px;letter-spacing:1.5px;color:var(--green-light);font-weight:600}
.cell svg.icon{position:absolute;left:22px;top:38px}
.review{padding-left:90px}
.review .name{font-size:19px;font-weight:600}
.review .date{font-size:9px;letter-spacing:1px;color:#333}
.review .stars{position:absolute;top:8px;left:200px;color:var(--green);font-size:18px;letter-spacing:3px}
.review p{font-size:13px;line-height:1.55;color:var(--body);margin-top:10px;width:250px}
.quote{font-family:Georgia,serif;font-size:140px;color:#e6e6ec;line-height:1}
.feature{top:2923px;height:268px;color:var(--white);padding:30px 24px}
.feature h4{font-size:17px;font-weight:700;line-height:1.3;width:120px}
.feature p{font-size:12px;line-height:1.5;margin-top:58px}
.feature svg{position:absolute;right:24px;top:30px}
.footer{left:0;top:3784px;width:1200px;height:311px;background:var(--navy);color:var(--white)}
.fcol h5{font-size:14px;font-weight:600;color:var(--green-light);margin-bottom:8px}
.fcol ul{list-style:none;border-left:2px solid var(--green-light);padding-left:10px;font-size:14px;line-height:1.45}
</style>
</head>
<body>

<section class="abs hero"></section>
<header class="abs nav">
  <div class="brand">Tumble Crate<br>Rentals Oz</div>
  <div class="nav-links">
    <span style="left:0">PRICING</span>
    <span style="left:127px">LEARN MORE</span>
    <span class="active" style="left:263px">ABOUT</span>
    <span style="left:401px">TRADE SECRETS</span>
    <span style="left:526px">CONTACT</span>
    <span style="left:720px">&#9707; CART</span>
    <span style="left:810px">LOG IN</span>
  </div>
</header>

<div class="abs sec-num" style="left:124px;top:210px">01</div>
<div class="abs rule" style="left:198px;top:218px;height:62px"></div>
<h1 class="abs sec-title" style="left:206px;top:216px;font-size:36px;color:var(--white)">1000's of Skips at Your Finger Tips</h1>
<div class="abs kicker" style="left:206px;top:264px;color:var(--green-light)">Best service &amp; price | Hassle free | Australia wide</div>
<div class="abs search" style="left:206px;top:298px;width:486px">
  <span class="field">Enter postcode or suburb</span>
  <span class="btn">SEARCH <span>&#8250;</span></span>
</div>

<!-- 02 process -->
<div class="abs photo" role="img" aria-label="Truck tipping a large skip bin" style="left:124px;top:542px;width:469px;height:248px"></div>
<div class="abs" style="left:593px;top:542px;width:480px;height:248px;background:var(--white)"></div>
<div class="abs sec-num" style="left:616px;top:630px">02</div>
<div class="abs rule" style="left:688px;top:636px;height:62px"></div>
<h2 class="abs sec-title" style="left:696px;top:634px;font-size:34px">As Easy As 1,2,3</h2>
<div class="abs kicker" style="left:696px;top:680px">Process</div>

<div class="abs step" style="left:124px;width:317px;background:var(--white)">
  <div class="n" style="color:var(--green)">1</div>
  <div class="lbl" style="color:var(--green)">Simple, easy booking</div>
  <p>Call 1800 555 017<br>or click here to get started with your instant quote</p>
</div>
<div class="abs step" style="left:441px;width:316px;background:var(--green);color:var(--white)">
  <div class="n">2</div>
  <div class="lbl">We confirm details</div>
  <p>Recive your booking details and a30 minute courtesy call before drop off</p>
</div>
<div class="abs step" style="left:757px;width:316px;background:var(--indigo);color:var(--white)">
  <div class="n" style="color:var(--green-light)">3</div>
  <div class="lbl" style="color:var(--green-light)">Gone when your ready</div>
  <p>Let us know and your bin will be gone whithin 24 hrs</p>
</div>
<svg class="abs" style="left:420px;top:880px" width="44" height="60" viewBox="0 0 44 60"><path d="M0 0 L22 0 L44 30 L22 60 L0 60 L22 30Z" fill="var(--green)"/></svg>
<svg class="abs" style="left:736px;top:880px" width="44" height="60" viewBox="0 0 44 60"><path d="M0 0 L22 0 L44 30 L22 60 L0 60 L22 30Z" fill="var(--green-light)"/></svg>

<!-- 03 how it works -->
<div class="abs sec-num" style="left:124px;top:1222px">03</div>
<div class="abs rule" style="left:196px;top:1228px;height:60px"></div>
<h2 class="abs sec-title" style="left:206px;top:1222px;font-size:34px">How it works?</h2>
<div class="abs kicker" style="left:206px;top:1268px">About us</div>
<p class="abs copy" style="left:206px;top:1306px;width:250px">Lorem ipsum dolor sit amet, consectetur adipisicing elit, sed do eiusmod tempor incididunt ut labore et dolore magna aliqua.</p>
<p class="abs copy" style="left:206px;top:1408px;width:250px">Ut enim ad minim veniam, quis nostrud exercitation ullamco laboris nisi ut aliquip ex ea commodo consequat.</p>
<div class="abs" role="img" aria-label="Explainer video still of a man standing beside a house" style="left:553px;top:1138px;width:520px;height:308px;background:linear-gradient(180deg,#c9cbe4 0%,#dfe0ee 60%,#6cbf6b 100%)"></div>
<svg class="abs" style="left:783px;top:1262px" width="60" height="60" viewBox="0 0 60 60"><circle cx="30" cy="30" r="28" fill="rgba(20,6,80,.75)"/><path d="M24 18 L42 30 L24 42Z" fill="#fff"/></svg>

<!-- 04 fields -->
<div class="abs cell" style="left:124px;top:1624px;width:475px;height:141px;background:var(--indigo)">
  <svg class="icon" width="56" height="56" viewBox="0 0 56 56" fill="none" stroke="var(--green-light)" stroke-width="2"><path d="M6 28 L28 8 L50 28"/><rect x="12" y="26" width="32" height="24"/><rect x="24" y="36" width="8" height="14"/></svg>
  <div class="tag">Renovator</div><div class="txt">Make sure skip bin hire is one less thing to worry about.</div><div class="more">READ MORE &#8250;</div>
</div>
<div class="abs" style="left:599px;top:1624px;width:474px;height:141px;background:var(--indigo-deep)"></div>
<div class="abs sec-num" style="left:616px;top:1660px;color:var(--green-light);opacity:.35">04</div>
<div class="abs rule" style="left:688px;top:1666px;height:60px"></div>
<h2 class="abs sec-title" style="left:696px;top:1660px;font-size:34px;color:var(--white)">For all your needs</h2>
<div class="abs kicker" style="left:696px;top:1706px;color:var(--green-light)">Fields</div>

<div class="abs cell" style="left:124px;top:1765px;width:475px;height:135px;background:var(--indigo-mid);border-top:1px solid #4a35b8">
  <svg class="icon" width="56" height="50" viewBox="0 0 56 50" fill="none" stroke="var(--green-light)" stroke-width="2"><rect x="6" y="14" width="44" height="30" rx="3"/><path d="M20 14 V8 H36 V14 M6 26 H50"/></svg>
  <div class="tag">Tradis</div><div class="txt">Hassle Free Skip Bin Hire</div><div class="more">READ MORE &#8250;</div>
</div>
<div class="abs cell" style="left:599px;top:1765px;width:474px;height:135px;background:var(--green)">
  <svg class="icon" width="56" height="50" viewBox="0 0 56 50" fill="none" stroke="#fff" stroke-width="2"><path d="M8 44 H48 M14 44 V20 H42 V44 M20 20 V10 H36 V20"/></svg>
  <div class="tag">Builder</div><div class="txt">Punctual, Professional and on your terms.</div><div class="more" style="color:#fff">READ MORE &#8250;</div>
</div>
<div class="abs cell" style="left:124px;top:1900px;width:475px;height:139px;background:var(--indigo);border-top:1px solid #4a35b8">
  <svg class="icon" width="56" height="50" viewBox="0 0 56 50" fill="none" stroke="var(--green-light)" stroke-width="2"><rect x="4" y="14" width="32" height="22"/><path d="M36 20 H46 L52 28 V36 H36"/><circle cx="14" cy="40" r="5"/><circle cx="44" cy="40" r="5"/></svg>
  <div class="tag">National</div><div class="txt">Your outsourced skip specialists</div><div class="more">READ MORE &#8250;</div>
</div>
<div class="abs cell" style="left:599px;top:1900px;width:474px;height:139px;background:var(--indigo);border-top:1px solid #4a35b8;border-left:1px solid #4a35b8">
  <svg class="icon" width="56" height="50" viewBox="0 0 56 50" fill="none" stroke="var(--green-light)" stroke-width="2"><rect x="6" y="14" width="40" height="30" rx="3"/><path d="M18 14 V8 H34 V14"/><circle cx="42" cy="38" r="9" fill="var(--indigo)"/><path d="M42 33 V38 H46"/></svg>
  <div class="tag">Corporate</div><div class="txt">You're busy and you need the job done. On-time and on-budget.</div><div class="more">READ MORE &#8250;</div>
</div>

<!-- 05 reviews -->
<div class="abs sec-num" style="left:124px;top:2152px">05</div>
<div class="abs rule" style="left:196px;top:2158px;height:60px"></div>
<h2 class="abs sec-title" style="left:206px;top:2152px;font-size:34px">Best client service</h2>
<div class="abs kicker" style="left:206px;top:2198px">Reviews</div>

<div class="abs" style="left:124px;top:2260px;width:633px;height:240px;background:var(--white)"></div>
<div class="abs quote" style="left:136px;top:2250px">&ldquo;</div>
<div class="abs review" style="left:116px;top:2288px">
  <div class="name">Daria</div><div class="date">19.02.2019</div><div class="stars">&#9733;&#9733;&#9733;&#9733;&#9733;</div>
  <p style="margin-left:-0px">Lorem ipsum dolor sit amet, consectetur adipisicing elit, sed do eiusmod tempor incididunt ut labore et dolore magna aliqua. Ut enim ad</p>
</div>
<div class="abs quote" style="left:436px;top:2250px">&ldquo;</div>
<div class="abs review" style="left:436px;top:2288px">
  <div class="name">Nick_19</div><div class="date">19.02.2019</div><div class="stars">&#9733;&#9733;&#9733;&#9733;&#9733;</div>
  <p>Lorem ipsum dolor sit amet, consectetur adipisicing elit, sed do eiusmod tempor incididunt ut labore et dolore magna aliqua. Ut enim ad</p>
</div>
<div class="abs" style="left:757px;top:2197px;width:316px;height:246px;background:var(--white)"></div>
<div class="abs quote" style="left:770px;top:2190px">&ldquo;</div>
<div class="abs review" style="left:748px;top:2226px">
  <div class="name">Lisa_Corpor</div><div class="date">19.02.2019</div><div class="stars">&#9733;&#9733;&#9733;&#9733;&#9733;</div>
  <p style="width:220px">Lorem ipsum dolor sit amet, consectetur adipisicing elit, sed do eiusmod tempor incididunt ut labore et dolore magna aliqua. Ut enim ad</p>
</div>
<svg class="abs" style="left:776px;top:2462px" width="50" height="30" viewBox="0 0 50 30" fill="none" stroke-width="2.5"><path d="M16 6 L8 15 L16 24" stroke="#999"/><path d="M24 4 V26" stroke="#bbb" stroke-width="1"/><path d="M32 6 L40 15 L32 24" stroke="var(--green)"/></svg>

<!-- 06 advantages -->
<div class="abs" role="img" aria-label="Smiling worker in a hard hat holding a tool" style="left:124px;top:2640px;width:469px;height:269px;background:linear-gradient(135deg,#8c8d92,#cfd0d4 50%,#a33a2c 100%)"></div>
<div class="abs" style="left:593px;top:2640px;width:480px;height:269px;background:var(--white)"></div>
<div class="abs sec-num" style="left:616px;top:2680px">06</div>
<div class="abs rule" style="left:688px;top:2686px;height:60px"></div>
<h2 class="abs sec-title" style="left:696px;top:2680px;font-size:34px">Real quality service</h2>
<div class="abs kicker" style="left:696px;top:2726px">Advantages</div>
<p class="abs copy" style="left:696px;top:2752px;width:320px">Lorem ipsum dolor sit amet, consectetur adipisicing elit, sed do eiusmod tempor incididunt ut labore et dolore magna aliqua. Ut enim ad minim veniam, quis nostrud exercitation ullamco laboris nisi ut aliquip ex ea commodo consequat.</p>

<div class="abs feature" style="left:124px;width:229px;background:var(--indigo)">
  <svg width="48" height="48" viewBox="0 0 48 48" fill="none" stroke="var(--green-light)" stroke-width="2"><circle cx="24" cy="18" r="9"/><path d="M8 44 C10 32 38 32 40 44"/><path d="M12 18 A12 12 0 0 1 36 18"/></svg>
  <h4>Service Guaranteed</h4>
  <p>Want to speak to someone when it suits you? We answer the phones and return calls from 7:30am to 8pm 7 days a week</p>
</div>
<div class="abs feature" style="left:367px;width:226px;background:var(--indigo)">
  <svg width="48" height="48" viewBox="0 0 48 48" fill="none" stroke="var(--green-light)" stroke-width="2"><path d="M6 18 H34 L30 40 H10Z"/><circle cx="36" cy="14" r="8"/><path d="M36 10 V14 H39"/></svg>
  <h4>Any Bin Anytime Anywhere</h4>
  <p>We connect you with local companies Australia wide; for faster response times, less km's and emissions, greater reliability and lower prices</p>
</div>
<div class="abs feature" style="left:604px;width:229px;background:var(--indigo)">
  <svg width="48" height="48" viewBox="0 0 48 48" fill="none" stroke="var(--green-light)" stroke-width="2"><ellipse cx="24" cy="28" rx="16" ry="12"/><path d="M18 16 H30 M40 26 H44 M14 38 V44 M32 38 V44"/><circle cx="24" cy="10" r="3"/></svg>
  <h4>Best Pricing</h4>
  <p>We've done the hard work behind the scenes, so with one click you have your best priced, local skip</p>
</div>
<div class="abs feature" style="left:844px;width:229px;background:var(--green)">
  <svg width="48" height="48" viewBox="0 0 48 48" fill="none" stroke="#fff" stroke-width="2"><circle cx="16" cy="14" r="6"/><circle cx="32" cy="14" r="6"/><path d="M4 40 C6 26 26 26 28 40 M22 40 C24 26 44 26 44 40"/></svg>
  <h4>First Class Supply Partners</h4>
  <p>Our local supply partners are the best in the business and share our passion for making you happy</p>
</div>

<!-- ready to go -->
<div class="abs" role="img" aria-label="Map of Australia" style="left:325px;top:3248px;width:550px;height:494px;border-radius:40% 45% 35% 40%;background:radial-gradient(ellipse at 50% 45%,#0d9443,#0a7f37)"></div>
<h2 class="abs sec-title" style="left:325px;top:3360px;width:550px;text-align:center;font-size:34px;color:var(--white)">We are ready to go!</h2>
<div class="abs kicker" style="left:325px;top:3408px;width:550px;text-align:center;color:var(--green-light)">Call us 7 days a week 7:30am to 8pm</div>
<div class="abs search" style="left:353px;top:3472px;width:494px">
  <span class="field">Enter postcode or suburb</span>
  <span class="btn">SEARCH <span>&#8250;</span></span>
</div>

<!-- footer -->
<footer class="abs footer">
  <div class="abs fcol" style="left:124px;top:50px">
    <h5>Australia Wide</h5>
    <ul><li>Sydney</li><li>Melbourne</li><li>Brisbane</li><li>Perth</li><li>Adelaide</li><li>Canberra</li></ul>
  </div>
  <div class="abs fcol" style="left:432px;top:50px">
    <h5>Learn more</h5>
    <ul><li>Waste Types</li><li>Skip Bin Sizes</li><li>Refund Policy</li><li>Pay Later with SplitPay</li><li>FAQ</li><li>Privacy</li></ul>
  </div>
  <div class="abs" style="left:751px;top:50px;width:322px">
    <div style="font-size:14px;font-weight:600;color:var(--green-light);line-height:1.4">Sign up for the latest news, offers<br>from TUMBLE CRATE RENTALS OZ</div>
    <div style="display:flex;margin-top:14px;height:38px;border:1px solid #fff">
      <span style="flex:1;font-size:13px;font-style:italic;padding:10px 8px;color:#ccc">Your Email</span>
      <span style="background:#fff;color:var(--navy);font-size:11px;font-weight:700;letter-spacing:1px;padding:11px 14px">SUBSCRIBE &#8250;</span>
    </div>
    <div style="display:flex;gap:26px;margin-top:22px">
      <span style="width:28px;height:28px;border-radius:50%;background:var(--green-light)"></span>
      <span style="width:28px;height:28px;border-radius:50%;background:var(--green-light)"></span>
      <span style="width:28px;height:28px;border-radius:50%;background:var(--green-light)"></span>
    </div>
  </div>
  <div class="abs" style="left:124px;top:256px;display:flex;gap:14px">
    <span style="width:44px;height:26px;border-radius:3px;background:#fff;opacity:.85"></span>
    <span style="width:44px;height:26px;border-radius:3px;background:#fff;opacity:.85"></span>
    <span style="width:44px;height:26px;border-radius:3px;background:#fff;opacity:.85"></span>
  </div>
  <div class="abs" style="left:666px;top:262px;font-size:13px">Copyright &copy; 2019, TUMBLE CRATE RENTALS OZ. Powered by Storefrontly</div>
</footer>
<div class="abs" style="left:0;top:4095px;width:1200px;height:140px;background:var(--white)"></div>

</body>
</html>
```